Tarvel Works - Powerpoint Templates

We are a consultancy to help builders to optimize their planning in order to save building costs. For that reason we need templates for teasers and presentations where we offer our services, show our team and their capacities and present workflows, organization charts, price lists etc.

```html
<!DOCTYPE html>
<html lang="en">
<head>
<meta charset="utf-8">
<title>Tarvel Works – Presentation Template</title>
<link href="https://fonts.googleapis.com/css2?family=Audiowide&family=Roboto:wght@400;700&display=swap" rel="stylesheet">
<style>
  :root {
    --page-black: #000000;
    --slide-dark: #1f1f22;
    --slide-dark-top: #2a2a2d;
    --gold: #c08a2a;
    --gold-deep: #a8700c;
    --gold-light: #d9a441;
    --ink: #2b2b2d;
    --body-ink: #333336;
    --white: #ffffff;
    --line: #9a9a9a;
    --card-shadow: rgba(0,0,0,0.18);
    --avatar-fill: #e9e9ec;
  }
  * { box-sizing: border-box; margin: 0; padding: 0; }
  html, body { width: 702px; height: 1200px; overflow: hidden; background: var(--page-black); }
  .canvas { position: relative; width: 702px; height: 1200px; }
  .slide { position: absolute; left: 23.5px; width: 652px; height: 367px; overflow: hidden; }
  .display { font-family: "Audiowide", sans-serif; }
  .text { font-family: "Roboto", sans-serif; }

  /* Title slide */
  .slide-title { top: 14px; background: linear-gradient(180deg, var(--slide-dark-top) 0%, var(--slide-dark) 60%, #1b1b1d 100%); }
  .title-brand { position: absolute; left: 0; right: 0; top: 150px; display: flex; justify-content: center; align-items: center; gap: 12px; }
  .brand-square { width: 30px; height: 30px; background: var(--gold); }
  .title-brand .brand-name { font-size: 34px; color: var(--gold); letter-spacing: 1px; }
  .project-title { position: absolute; left: 0; right: 0; top: 249px; text-align: center; font-size: 25px; color: var(--gold); letter-spacing: 2px; word-spacing: 6px; }
  .presenter-name { position: absolute; left: 0; right: 0; top: 286px; text-align: center; font-size: 17px; color: var(--white); letter-spacing: 1.5px; word-spacing: 5px; }

  /* Content slides */
  .slide-content { background: var(--white); }
  .slide-about { top: 413px; }
  .slide-chart { top: 809px; }
  .header-marker { position: absolute; left: 0; top: 15px; width: 7px; height: 32px; background: var(--ink); }
  .slide-heading { position: absolute; left: 20px; top: 21px; font-size: 17px; color: var(--ink); letter-spacing: 0.5px; word-spacing: 4px; }
  .slide-heading .accent { color: var(--gold); }
  .corner-brand { position: absolute; right: 10px; top: 24px; display: flex; align-items: center; gap: 6px; }
  .corner-brand .brand-square { width: 12px; height: 12px; }
  .corner-brand .brand-name { font-size: 14px; color: var(--gold); }

  .feature-brand { position: absolute; left: 17px; top: 85px; width: 212px; height: 220px; display: flex; flex-direction: column; justify-content: center; align-items: flex-start; gap: 10px; }
  .feature-brand .brand-square { width: 44px; height: 44px; }
  .feature-brand .brand-name { font-size: 34px; line-height: 1.1; color: var(--gold); }

  .about-copy { position: absolute; left: 255px; top: 82px; width: 385px; font-size: 8.2px; line-height: 15.3px; color: var(--body-ink); }
  .about-copy p + p { margin-top: 15.3px; }

  .slide-footer { position: absolute; left: 0; right: 0; bottom: 0; height: 23px; background: linear-gradient(90deg, var(--gold-deep) 0%, #b5790f 70%, var(--gold-light) 100%); }
  .copyright { position: absolute; left: 14px; top: 4px; font-size: 11px; color: var(--white); }
  .page-tab { position: absolute; right: 0; top: 0; width: 86px; height: 23px; background: var(--ink); }
  .page-tab-svg { position: absolute; right: 54px; top: 0; }
  .page-label { position: absolute; right: 9px; top: 4px; font-size: 11px; font-weight: 700; color: var(--white); }

  /* Org chart */
  .org-lines { position: absolute; left: 0; top: 0; }
  .org-card { position: absolute; width: 77px; height: 52px; background: var(--white); border-radius: 2px; box-shadow: 0 2px 4px var(--card-shadow); text-align: center; }
  .org-card::before { content: ""; position: absolute; left: 0; right: 0; top: 0; height: 5px; background: var(--gold); border-radius: 2px 2px 0 0; }
  .avatar { position: absolute; left: 20.5px; top: -20px; width: 36px; height: 36px; border-radius: 50%; background: var(--avatar-fill); border: 3px solid var(--gold-light); }
  .card-title { position: absolute; left: 0; right: 0; top: 19px; font-size: 7px; color: var(--ink); }
  .card-note { position: absolute; left: 12px; right: 12px; top: 29px; font-size: 3.6px; line-height: 4.3px; color: #777; }
</style>
</head>
<body>
<main class="canvas">

  <section class="slide slide-title">
    <div class="title-brand">
      <span class="brand-square"></span>
      <span class="brand-name display">TARVEL WORKS</span>
    </div>
    <h1 class="project-title display">PROJECT TITLE HERE</h1>
    <p class="presenter-name display">PERSENTATOR NAME HERE</p>
  </section>

  <section class="slide slide-content slide-about">
    <span class="header-marker"></span>
    <h2 class="slide-heading display">ABOUT OUR <span class="accent">TARVEL WORKS</span></h2>
    <div class="corner-brand"><span class="brand-square"></span><span class="brand-name display">TARVEL WORKS</span></div>

    <div class="feature-brand">
      <span class="brand-square"></span>
      <span class="brand-name display">TARVEL<br>WORKS</span>
    </div>

    <div class="about-copy text">
      <p>Lorem ipsum dolor sit amet, consectetur adipisicing elit, sed do eiusmod tempor incididunt ut labore et dolore magna aliqua. Ut enim ad minim veniam, quis nostrud exercitation ullamco laboris nisi ut aliquip ex ea commodo consequat.</p>
      <p>Excepteur sint occaecat cupidatat non proident, sunt in culpa qui officia deserunt mollit anim id est laborum. Sed ut perspiciatis unde omnis iste natus error sit voluptatem accusantium doloremque laudantium, totam rem aperiam, eaque ipsa quae ab illo inventore veritatis et quasi architecto beatae vitae dicta sunt explicabo.</p>
      <p>Lorem ipsum dolor sit amet, consectetur adipisicing elit, sed do eiusmod tempor incididunt ut labore et dolore magna aliqua. Ut enim ad minim veniam, quis nostrud exercitation ullamco laboris nisi ut aliquip ex ea commodo consequat.</p>
      <p>Excepteur sint occaecat cupidatat non proident, sunt in culpa qui officia deserunt mollit anim id est laborum.</p>
    </div>

    <footer class="slide-footer">
      <span class="copyright text">Copyright text here</span>
      <svg class="page-tab-svg" width="40" height="23" viewBox="0 0 40 23"><polygon points="0,0 40,0 40,23 32,23" fill="#2b2b2d"/><polygon points="5,0 10,0 40,23 33,23" fill="#ffffff"/></svg>
      <span class="page-tab"></span>
      <span class="page-label text">Page : 01</span>
    </footer>
  </section>

  <section class="slide slide-content slide-chart">
    <span class="header-marker"></span>
    <h2 class="slide-heading display">ABOUT OUR <span class="accent">TARVEL WORKS</span></h2>
    <div class="corner-brand"><span class="brand-square"></span><span class="brand-name display">TARVEL WORKS</span></div>

    <svg class="org-lines" width="652" height="367" viewBox="0 0 652 367" fill="none" stroke="#9a9a9a" stroke-width="0.8">
      <polyline points="290,100 215,100 215,148"/>
      <polyline points="367,100 442,100 442,148"/>
      <polyline points="177,199 160,199 160,247"/>
      <polyline points="254,199 270,199 270,247"/>
      <polyline points="404,199 387,199 387,247"/>
      <polyline points="481,199 497,199 497,247"/>
    </svg>

    <div class="org-card text" style="left:290px; top:74px;">
      <span class="avatar" role="img" aria-label="Team member portrait"></span>
      <span class="card-title">Sample text</span>
      <span class="card-note">Lead planner for cost and site review</span>
    </div>

    <div class="org-card text" style="left:177px; top:173px;">
      <span class="avatar" role="img" aria-label="Team member portrait"></span>
      <span class="card-title">Sample text</span>
      <span class="card-note">Lead planner for cost and site review</span>
    </div>
    <div class="org-card text" style="left:404px; top:173px;">
      <span class="avatar" role="img" aria-label="Team member portrait"></span>
      <span class="card-title">Sample text</span>
      <span class="card-note">Lead planner for cost and site review</span>
    </div>

    <div class="org-card text" style="left:121px; top:271px;">
      <span class="avatar" role="img" aria-label="Team member portrait"></span>
      <span class="card-title">Sample text</span>
      <span class="card-note">Lead planner for cost and site review</span>
    </div>
    <div class="org-card text" style="left:231px; top:271px;">
      <span class="avatar" role="img" aria-label="Team member portrait"></span>
      <span class="card-title">Sample text</span>
      <span class="card-note">Lead planner for cost and site review</span>
    </div>
    <div class="org-card text" style="left:348px; top:271px;">
      <span class="avatar" role="img" aria-label="Team member portrait"></span>
      <span class="card-title">Sample text</span>
      <span class="card-note">Lead planner for cost and site review</span>
    </div>
    <div class="org-card text" style="left:458px; top:271px;">
      <span class="avatar" role="img" aria-label="Team member portrait"></span>
      <span class="card-title">Sample text</span>
      <span class="card-note">Lead planner for cost and site review</span>
    </div>

    <footer class="slide-footer">
      <span class="copyright text">Copyright text here</span>
      <svg class="page-tab-svg" width="40" height="23" viewBox="0 0 40 23"><polygon points="0,0 40,0 40,23 32,23" fill="#2b2b2d"/><polygon points="5,0 10,0 40,23 33,23" fill="#ffffff"/></svg>
      <span class="page-tab"></span>
      <span class="page-label text">Page : 01</span>
    </footer>
  </section>

</main>
</body>
</html>
```